Broschüre für Immobilienmakler
Tolverido hat unsere Vorstellungen erkannt und von Beginn an super umgesetzt. Natürlich waren noch nachträgliche Änderungen und Feinabstimmungen notwendig. Diese wurden wunschgemäß perfektioniert. Man hatte hier wirklich sehr schöne Ideen in den Details ohne den Blick auf das Ganze zu verlieren. Dadurch haben wir jetzt eine perfekte Broschüre erhalten. Das war bestimmt nicht unser letztes Projekt. Vielen Dank
Zielgruppe
Wir sind Immobilienmakler & Home Stager; unsere hauptsächliche Zielgruppe sind Personen, die Ihre Immobilie verkaufen möchten. Die Broschüre soll ein wichtiger Teil der Akquise werden. Wir vermitteln als Immobilienmakler ganz ursprünglich, jedoch bieten wir auch den gesamten Service rund um den Verkauf (Einholung Unterlagen, Präsentieren der Immobilie durch kleine Effekte bis hin zu Entrümpelungen und Renovierung inkl. Einrichtungsbeispiele/Deko). Zudem sind wir jeden Tag (auch Sonn-und Feiertags) für unsere Kunden erreichbar und auch in Terminen. (Eindrücke gibt es auch über unsere Vombalo-Bewertungen)
Aufgabenstellung
Wir möchten einerseits natürlich mit unseren Vorzügen ggü. den 'Standard-Maklern' werben, aber auch genauso professionell den 'Standard-Dienst' ohne Home-Staging anbieten. (Viele Kunden denken schnell, dass wir nur außergewöhnliche und arbeitsintensive Objekte annehmen).
Texte würden wir versuchen zu übernehmen (hier würden wir die vorgesehenen Textfelder der Designer nutzen) und Bilder müssten vermutlich abgesprochen werden, da wir nicht sicher sind, ob unser Material dafür ausreicht. Die Bilder der Homepage liegen hier vor und können gerne zusätzlich gesendet werden.
Unsere Schriftart ist die Museo Sans rounded

```html
<!DOCTYPE html>
<html lang="de">
<head>
<meta charset="utf-8">
<title>Raumglück – Broschüre</title>
<link href="https://fonts.googleapis.com/css2?family=Nunito:wght@400;600;700;800;900&display=swap" rel="stylesheet">
<style>
:root{
  --stage:#7d7d7d;
  --purple:#9b88ad;
  --purple-deep:#8a76a0;
  --lavender:#efeaf3;
  --lavender-mid:#ddd3e6;
  --dark:#2b1f1f;
  --ink:#2a2a2a;
  --white:#ffffff;
}
*{margin:0;padding:0;box-sizing:border-box}
html,body{width:1200px;height:2317px;overflow:hidden}
body{background:var(--stage);font-family:"Nunito",sans-serif;color:var(--ink);position:relative}
.spread{position:absolute;left:0;width:1200px;height:846px;overflow:hidden;background:linear-gradient(180deg,var(--white),var(--lavender))}
.spread--outer{top:292px}
.spread--inner{top:1178px;background:var(--white)}
.shapes{position:absolute;inset:0}
.abs{position:absolute}

/* outer spread */
.brand{position:absolute;display:flex;align-items:center;gap:10px;color:var(--dark);font-weight:800;letter-spacing:1px}
.brand__dot{border-radius:50%;background:var(--purple)}
.brand--small{left:70px;top:255px;font-size:26px}
.brand--small .brand__dot{width:16px;height:16px}
.brand--large{left:815px;top:395px;font-size:44px}
.brand--large .brand__dot{width:26px;height:26px}
.contact{left:69px;top:436px;width:260px}
.contact__names{color:var(--purple);font-weight:800;font-size:21px}
.contact__role{font-weight:800;font-size:14px;line-height:1.2;margin-top:10px;color:var(--dark)}
.contact__list{list-style:none;margin-top:8px}
.contact__list li{display:flex;align-items:flex-start;gap:12px;font-size:15px;line-height:1.2;margin-bottom:12px;color:var(--dark)}
.contact__list li svg{flex:0 0 16px;margin-top:1px}
.contact__web{color:var(--purple);font-weight:700}
.portrait{background:linear-gradient(180deg,#cfcfcf,#5a5a5a);border-radius:46% 46% 0 0/28% 28% 0 0}
.portrait--him{left:305px;top:383px;width:285px;height:463px}
.portrait--her{left:635px;top:412px;width:258px;height:434px}
.claim{left:902px;top:648px;color:var(--white);font-weight:900;font-size:25px;line-height:1.05;text-transform:uppercase}
.claim small{display:block;font-size:16px;font-weight:800;margin-top:6px}
.weblink{color:var(--white);font-weight:800;font-size:19px}
.weblink--outer{left:902px;top:786px}

/* inner spread */
.section-title{left:69px;top:30px;color:var(--white);font-weight:900;font-size:20px;letter-spacing:.5px}
.reviews{left:655px;top:16px;width:525px;color:var(--white);text-align:center}
.reviews__title{display:flex;align-items:center;gap:14px;justify-content:center;font-weight:800;font-size:20px}
.reviews__title span{flex:1;height:2px;background:var(--white)}
.reviews__quote{font-size:11px;font-weight:700;line-height:1.7;margin-top:2px}
.reviews__mark{font-size:22px;font-weight:900;line-height:.8}
.services{top:172px}
.services--sale{left:51px;width:245px}
.services--rent{left:325px;width:230px}
.services__head{background:var(--purple);color:var(--white);font-weight:900;font-size:13px;padding:3px 12px;width:120px;border-bottom:3px solid var(--purple)}
.services__rule{height:3px;background:var(--lavender-mid);margin-top:-3px;margin-left:120px}
.services__list{list-style:none;margin-top:10px}
.services__list li{position:relative;padding-left:25px;font-size:11.5px;line-height:1.15;margin-bottom:9px;color:var(--dark)}
.services__list li::before{content:"";position:absolute;left:0;top:1px;width:11px;height:11px;border-radius:50%;background:var(--purple)}
.services__list li::after{content:"";position:absolute;left:3.5px;top:3px;width:3px;height:5px;border:solid var(--white);border-width:0 1.5px 1.5px 0;transform:rotate(45deg)}
.services__sub{color:var(--purple);font-weight:800;font-size:14px;line-height:1.05;margin:16px 0 6px}
.services__note{color:var(--purple);font-weight:800;font-size:11px;line-height:1.2;margin-top:14px}
.house-photo{left:605px;top:278px;width:595px;height:416px;background:radial-gradient(ellipse at 35% 45%,#6c7079 0%,#a9acb4 28%,#e6d0bf 52%,rgba(255,255,255,0) 75%)}
.perks{left:950px;top:297px;list-style:none}
.perks li{position:relative;padding-left:24px;font-weight:900;font-size:15.5px;line-height:1.05;color:var(--dark);margin-bottom:20px;text-transform:uppercase}
.perks li::before{content:"";position:absolute;left:0;top:2px;width:12px;height:12px;border-radius:50%;background:var(--purple)}
.perks li::after{content:"";position:absolute;left:4px;top:4px;width:3px;height:6px;border:solid var(--white);border-width:0 1.5px 1.5px 0;transform:rotate(45deg)}
.weblink--inner{left:820px;top:640px;color:var(--purple)}
.gallery{left:0;top:694px;width:1200px;height:152px;display:flex;gap:0}
.gallery__item{flex:1;border-right:2px solid var(--white)}
.gallery__item:last-child{border-right:0}
</style>
</head>
<body>

<section class="spread spread--outer" aria-label="Außenseite der Broschüre">
  <svg class="shapes" viewBox="0 0 1200 846" width="1200" height="846">
    <path d="M0 150 C120 210,200 250,260 270 L260 300 C160 270,70 240,0 200 Z" fill="var(--purple)" opacity=".75"/>
    <path d="M214 0 H1157 C1080 210,840 350,560 345 C400 340,270 270,214 190 Z" fill="var(--purple)"/>
    <path d="M0 770 C150 740,260 745,330 760 L330 846 H0 Z" fill="var(--lavender-mid)"/>
    <path d="M0 800 C120 790,220 800,300 815 L300 846 H0 Z" fill="var(--purple)"/>
    <path d="M600 846 C740 640,950 560,1200 590 V846 Z" fill="var(--purple)"/>
    <path d="M560 846 C700 600,940 520,1200 560 V590 C950 555,740 630,600 846 Z" fill="var(--dark)"/>
  </svg>
  <div class="abs" role="img" aria-label="Foto eines hellen Wohnraums mit Regal, Palme, Bildern und Treppe" style="left:214px;top:0;width:943px;height:335px;clip-path:path('M0 0 H943 C866 200,626 336,346 331 C186 326,56 260,0 180 Z');background:linear-gradient(160deg,#e8e4e0 0%,#f6f5f3 40%,#dfe3da 60%,#c8c4bc 100%)"></div>

  <div class="brand brand--small"><span class="brand__dot"></span>RAUMGLÜCK</div>

  <div class="abs contact">
    <p class="contact__names">Lisanne &amp; Jorin Velt</p>
    <p class="contact__role">Immobilienmakler/<br>in Home Stager/in (IHK)</p>
    <ul class="contact__list">
      <li><svg width="16" height="16" viewBox="0 0 16 16"><path d="M8 1a5 5 0 0 0-5 5c0 4 5 9 5 9s5-5 5-9a5 5 0 0 0-5-5zm0 7a2 2 0 1 1 0-4 2 2 0 0 1 0 4z" fill="var(--purple)"/></svg><span>Lindenweg 14<br>42999 Velbrück</span></li>
      <li><svg width="16" height="16" viewBox="0 0 16 16"><circle cx="8" cy="8" r="8" fill="var(--purple)"/><path d="M5 4l2 2-1 1c.5 1 1.5 2 3 3l1-1 2 2-1.5 1.5C7 12 4 9 3.5 5.5z" fill="#fff"/></svg><span>02190 – 55 10 925</span></li>
      <li><svg width="16" height="16" viewBox="0 0 16 16"><circle cx="8" cy="8" r="8" fill="var(--purple)"/><path d="M5 4l2 2-1 1c.5 1 1.5 2 3 3l1-1 2 2-1.5 1.5C7 12 4 9 3.5 5.5z" fill="#fff"/></svg><span>02190 – 55 10 926</span></li>
      <li><svg width="16" height="16" viewBox="0 0 16 16"><circle cx="8" cy="8" r="8" fill="var(--purple)"/><rect x="4" y="5" width="8" height="6" fill="none" stroke="#fff" stroke-width="1.2"/><path d="M4 5l4 3 4-3" fill="none" stroke="#fff" stroke-width="1.2"/></svg><span>velt@raumglueck.info</span></li>
      <li><svg width="16" height="16" viewBox="0 0 16 16"><circle cx="8" cy="8" r="8" fill="var(--purple)"/><circle cx="8" cy="8" r="4.5" fill="none" stroke="#fff" stroke-width="1.1"/><path d="M3.5 8h9M8 3.5c-2 2.5-2 6.5 0 9M8 3.5c2 2.5 2 6.5 0 9" fill="none" stroke="#fff" stroke-width="1"/></svg><span class="contact__web">www.raumglueck.info</span></li>
    </ul>
  </div>

  <div class="abs portrait portrait--him" role="img" aria-label="Schwarz-weiß Porträt des Maklers mit verschränkten Armen"></div>
  <div class="abs portrait portrait--her" role="img" aria-label="Schwarz-weiß Porträt der Home Stagerin im karierten Blazer"></div>

  <div class="brand brand--large"><span class="brand__dot"></span>RAUMGLÜCK</div>

  <p class="abs claim">Home Stager<br>Immobilienmakler<small>aus Velbrück</small></p>
  <p class="abs weblink weblink--outer">www.raumglueck.info</p>
</section>

<section class="spread spread--inner" aria-label="Innenseite der Broschüre">
  <svg class="shapes" viewBox="0 0 1200 846" width="1200" height="846">
    <path d="M0 0 H1200 V245 C1000 220,850 203,660 167 C500 135,300 105,120 115 C70 120,30 135,0 150 Z" fill="var(--purple)"/>
    <path d="M120 112 C300 100,500 130,660 162 C850 198,1000 215,1200 240 V268 C1000 240,850 222,660 184 C500 150,300 118,120 112 Z" fill="var(--dark)"/>
  </svg>
  <div class="abs" role="img" aria-label="Blasses Foto eines Hausdachs im Hintergrund" style="left:640px;top:0;width:560px;height:200px;background:linear-gradient(120deg,rgba(255,255,255,.15),rgba(255,255,255,0));"></div>

  <h2 class="abs section-title">UNSERE LEISTUNGEN FÜR SIE:</h2>

  <div class="abs reviews">
    <p class="reviews__title"><span></span>Warum Kunden auf uns setzen<span></span></p>
    <p class="reviews__mark">“</p>
    <p class="reviews__quote">Sehr professionelle Abwicklung. Wir hatten ein rundum Sorglospaket von der<br>Firma Raumglück. Über ausräumen, kleinere Renovierungsarbeiten und<br>geschmackvolle Einrichtung des Hauses haben sie die Immobilie innerhalb weniger<br>Tage nach zahlreichen Anfragen erfolgreich verkauft. Der Kontakt war immer<br>sehr nett. Super, machen sie weiter so.</p>
    <p class="reviews__mark">”</p>
  </div>

  <div class="abs services services--sale">
    <p class="services__head">VERKAUF:</p><div class="services__rule"></div>
    <ul class="services__list">
      <li>Kostenlose Erstberatung</li>
      <li>Kostenlose Verkehrswertermittlung</li>
      <li>Kostenlose Erstellung eines<br>Energieausweises bei Verkauf</li>
      <li>Ansprechende professionelle Fotos</li>
      <li>Optionale Luftaufnahmen</li>
      <li>Besorgungen der notwendigen<br>Verkaufsunterlagen</li>
      <li>Objektaufbereitung</li>
      <li>Wettbewerbsanalyse</li>
      <li>Zielgruppenanalyse</li>
      <li>Werbe- und Marketingkonzept</li>
      <li>Flyer / Nachbarschaftswerbung<br>(auf Wunsch)</li>
      <li>Verkaufsschild (auf Wunsch)</li>
      <li>Besichtigungen / optional als<br>Open House inkl. Sektempfang</li>
      <li>Unterstützung und Betreuung</li>
      <li>Von der Beratung bis zur Übergabe</li>
      <li>Inserate in verschiedenen Medien</li>
      <li>Grundriss Erstellung (auf Wunsch)</li>
      <li>Sehr gute lokale Marktkenntnisse</li>
    </ul>
  </div>

  <div class="abs services services--rent">
    <p class="services__head">VERMIETUNG:</p><div class="services__rule"></div>
    <ul class="services__list">
      <li>Kostenlose Erstberatung</li>
      <li>Ansprechende<br>professionelle Fotos</li>
      <li>Unterstützung und Betreuung<br>von der Beratung bis zur<br>Übergabe</li>
      <li>Komplette Korrespondenz<br>mit Interessenten</li>
      <li>Inserate in<br>verschiedenen Medien</li>
      <li>Fertigung der Mietverträge</li>
    </ul>
    <p class="services__sub">Zusätzliche Leistungen<br>für den Verkauf:</p>
    <ul class="services__list">
      <li>Home Staging</li>
      <li>Ausräumen der<br>Verkaufsimmobilie</li>
      <li>Renovierungsarbeiten</li>
      <li>Kleine Reparaturarbeiten</li>
      <li>Gartenpflege</li>
      <li>Grundreinigung</li>
    </ul>
    <p class="services__note">Zusätzlicher Service des Home<br>Staging ist möglich</p>
  </div>

  <div class="abs house-photo" role="img" aria-label="Hand hält ein kleines Hausmodell mit Schlüssel"></div>

  <ul class="abs perks">
    <li>Kostenlose<br>Wertermittlung</li>
    <li>Kostenloser<br>Energieausweis<br>bei Verkauf</li>
    <li>Kostenlose<br>Erstberatung</li>
  </ul>

  <p class="abs weblink weblink--inner">www.raumglueck.info</p>

  <div class="abs gallery">
    <div class="gallery__item" role="img" aria-label="Foto Wohnzimmer mit Hängesessel" style="background:linear-gradient(180deg,#5a4a3e,#e9e6e2 45%,#cfd2d6)"></div>
    <div class="gallery__item" role="img" aria-label="Foto Flur mit Palme und Truhe" style="background:linear-gradient(180deg,#f1efec,#d8d4cc 70%,#5d5047)"></div>
    <div class="gallery__item" role="img" aria-label="Foto Terrasse mit Garten" style="background:linear-gradient(180deg,#3d3c38,#6f8a4e 50%,#c9c1b3)"></div>
    <div class="gallery__item" role="img" aria-label="Foto Dachgeschoss mit Holzdecke" style="background:linear-gradient(180deg,#a57a4d,#e9e4de 55%,#b88a5a)"></div>
    <div class="gallery__item" role="img" aria-label="Foto heller Wohnraum mit Parkett" style="background:linear-gradient(180deg,#f4f3f1,#e6e3e0 55%,#c29a6c)"></div>
    <div class="gallery__item" role="img" aria-label="Foto Essbereich mit Fensterfront" style="background:linear-gradient(180deg,#3a3430,#d8dad3 45%,#bdb6ac)"></div>
  </div>
</section>

</body>
</html>
```